Flyer für Betreuungsleistungen und Verhinderungspflege erstellen
Zielgruppe
wir sind ein mobiler Pflegedienst in Rostock und versorgen Patienten in der Häuslichkeit.
Aufgabenstellung
Es soll ein Flyer erstellt werde mit folgendem Text:
5 Weitere Punkte folgen noch. Der Flyer soll seriös und exklusiv wirken.
Unsere Betreuungsangebote
Wenn Sie eine Pflegestufe haben, können Sie auf verschiedene Angebote der Betreuung Nutzen.
Betreuungsleistungen und die Leistungen der Verhinderungspflege sollen für Pflegebedürftige unter anderem aktivierende und qualitätsgesicherte Betreuungsangebote verfügbar machen und pflegenden Angehörigen eine Möglichkeit der Entlastung bieten.
Die Leistungen können auch von Patienten in Anspruch genommen werden, die Pflegegeld in Anspruch nehmen und sich nicht der Hilfe eines Pflegedienstes bedienen. Das Budget wird zusätzlich zum Pflegegeld zur Verfügung gestellt.
Bewegung:
Da pflegebedürftige Menschen zu sozialem Rückzug und zur körperlichen Versteifung neigen, sind körperliche Aktivitäten wie Bewegungsspiele und eine kontinuierliche uns konsequente Anleitung zur Mobilität besonders wichtig. Dabei hilft nicht nur, mobil zu bleiben und Energie zu lenken. Da Wahrnehmung und Bewegung voneinander Unabhängig sind, fördert Bewegung die Wahrnehmung sowie den Kontakt zur Umwelt und vermindert damit Anspannung, Ängste und Aggressionen.
_ 5 weitere Punkte folgen noch---

```html
<!DOCTYPE html>
<html lang="de">
<head>
<meta charset="utf-8">
<title>Pflegedienst Hafenblick – Flyer</title>
<link href="https://fonts.googleapis.com/css2?family=Open+Sans:wght@400;600;700&display=swap" rel="stylesheet">
<style>
:root{
  --green:#4aa63a;
  --orange:#e39a1f;
  --blue:#1b5fa8;
  --ink:#2b2b2b;
  --box:rgba(255,255,255,.9);
}
*{box-sizing:border-box;margin:0;padding:0}
html,body{width:849px;height:1200px;overflow:hidden;background:#fff}
body{font-family:"Open Sans",sans-serif;color:var(--ink)}
.spread{position:absolute;left:0;width:849px;height:600px;display:flex}
.spread--outside{top:0}
.spread--inside{top:600px}
.panel{position:relative;width:283px;height:600px;overflow:hidden;
  background:radial-gradient(ellipse at 60% 30%,#fafbfc 0%,#e7eaed 55%,#d9dde1 100%);
  border-right:1px solid #d0d4d8}
.panel:last-child{border-right:none}
.stack{position:absolute;left:20px;right:20px;display:flex;flex-direction:column;gap:28px}
.box{position:relative;background:var(--box);border-radius:14px;padding:22px 16px 14px;
  box-shadow:0 1px 4px rgba(0,0,0,.08)}
.box--tag-bottom{padding-bottom:24px}
.box p{font-size:9px;line-height:1.42;margin-bottom:7px}
.box p:last-of-type{margin-bottom:0}
.tag{position:absolute;color:#fff;font-weight:700;font-size:10.5px;padding:4px 14px;border-radius:3px 9px 3px 9px;white-space:nowrap;line-height:1.2}
.tag--top-right{top:-11px;right:16px}
.tag--top-left{top:-11px;left:0}
.tag--bottom-left{bottom:-11px;left:10px}
.tag--green{background:var(--green)}
.tag--orange{background:var(--orange)}
.tag--blue{background:var(--blue)}
.brand{position:absolute;display:flex;align-items:center;flex-direction:column;gap:8px}
.brand__dot{width:22px;height:22px;border-radius:50%;background:var(--green);flex:none}
.brand__name{font-weight:700;font-size:14px;color:var(--green);line-height:1.15;text-align:center}
.photo{position:absolute}
.contact{position:absolute;left:30px;top:210px;width:223px;height:260px;background:var(--box);border-radius:14px;box-shadow:0 1px 4px rgba(0,0,0,.08)}
.contact__lines{position:absolute;top:120px;width:100%;text-align:center;font-size:10px;line-height:1.5}
.contact__phone{position:absolute;left:-6px;right:-6px;bottom:14px;background:var(--blue);color:#fff;font-weight:600;font-size:11px;padding:6px 12px;border-radius:3px 10px 3px 10px;display:flex;align-items:center;gap:8px}
.cover-tags{position:absolute;right:14px;top:485px;display:flex;flex-direction:column;align-items:flex-end;gap:8px}
.cover-tags .tag{position:static;font-size:11px}
</style>
</head>
<body>

<section class="spread spread--outside">
  <div class="panel">
    <div class="stack" style="top:62px">
      <div class="box">
        <span class="tag tag--green tag--top-right">Lorem Ipsum</span>
        <p>Arum exerae etusda sum veliqui unt. Qui qui atiat fugia secessequam ratia dolendi tatibustrum ilibusani re, sa cus, sitaerr uptatur, a consequae nihicae. Nem dicit facis etum eatet eaqui berum doloruptur recero bernam.</p>
        <p>Quas dolenis rem quiaspe ribust omnihicil id ullab il ilique verum derum lab iuntem et andi velitatio quia sinusam invelitam atius expelitiores simagnam et reius. Nulpa sitiam solorent maion.</p>
      </div>
      <div class="box">
        <span class="tag tag--orange tag--top-left">Lorem Ipsum</span>
        <p>Arum exerae etusda sum veliqui unt. Qui qui atiat fugia secessequam ratia dolendi tatibustrum ilibusani re, sa cus, sitaerr uptatur, a consequae.</p>
        <p>Nihicae. Nem dicit facis etum eatet eaqui berum doloruptur recero bernam, cor autemolesti tem quas dolenis rem quiaspe ribust omnihicil id ullab il ilique verum derum lab iuntem et andi velitatio quia sinusam invelitam.</p>
      </div>
    </div>
    <div class="photo" role="img" aria-label="Foto: zwei ältere Menschen spielen lachend Karten"
      style="left:-60px;top:470px;width:290px;height:290px;border-radius:50%;border:4px solid var(--blue);background:linear-gradient(135deg,#e8ddd0,#b7c2cf 55%,#f0d6cc)"></div>
  </div>

  <div class="panel">
    <div class="contact">
      <div class="brand" style="left:0;right:0;top:30px">
        <span class="brand__dot" style="width:40px;height:40px"></span>
        <span class="brand__name">Pflegedienst<br>Hafenblick</span>
      </div>
      <div class="contact__lines">
        Lindenweg 24<br>18057 Rostock<br>0381 4455210<br>info@pflegedienst-hafenblick.de<br>www.pflegedienst-hafenblick.de
      </div>
      <div class="contact__phone">
        <svg width="12" height="12" viewBox="0 0 24 24" aria-hidden="true"><path fill="#fff" d="M6.6 10.8a15 15 0 0 0 6.6 6.6l2.2-2.2c.3-.3.7-.4 1-.2 1.1.4 2.3.6 3.6.6.6 0 1 .4 1 1V20c0 .6-.4 1-1 1A17 17 0 0 1 3 4c0-.6.4-1 1-1h3.5c.6 0 1 .4 1 1 0 1.3.2 2.5.6 3.6.1.3 0 .7-.2 1z"/></svg>
        0800 1234 567 (kostenfrei)
      </div>
    </div>
  </div>

  <div class="panel">
    <div class="brand" style="left:0;right:0;top:40px">
      <span class="brand__dot" style="width:50px;height:50px"></span>
      <span class="brand__name" style="font-size:17px">Pflegedienst<br>Hafenblick</span>
    </div>
    <svg class="photo" style="left:0;top:170px" width="283" height="430" viewBox="0 0 283 430" role="img" aria-label="Foto: lächelnde Pflegerin umarmt eine ältere Dame">
      <defs><linearGradient id="coverPhoto" x1="0" y1="0" x2="1" y2="1">
        <stop offset="0" stop-color="#e9d8c8"/><stop offset=".5" stop-color="#f3e4da"/><stop offset="1" stop-color="#2f6ea8"/></linearGradient></defs>
      <path d="M0 70 Q130 10 283 40 L283 430 L0 430 Z" fill="url(#coverPhoto)"/>
      <path d="M0 70 Q130 10 283 40" fill="none" stroke="#1b5fa8" stroke-width="5"/>
    </svg>
    <div class="cover-tags">
      <span class="tag tag--green">Pflege bedeutet Verantwortung</span>
      <span class="tag tag--orange" style="margin-right:26px">Wir kümmern uns um Sie</span>
    </div>
  </div>
</section>

<section class="spread spread--inside">
  <div class="panel">
    <div class="stack" style="top:70px">
      <div class="box">
        <span class="tag tag--orange tag--top-left">Unsere Betreuungsangebote</span>
        <p>Wenn Sie eine Pflegestufe haben, können Sie auf verschiedene Angebote der Betreuung Nutzen.</p>
        <p>Betreuungsleistungen und die Leistungen der Verhinderungspflege sollen für Pflegebedürftige unter anderem aktivierende und qualitätsgesicherte Betreuungsangebote verfügbar machen und pflegenden Angehörigen eine Möglichkeit der Entlastung bieten.</p>
        <p>Die Leistungen können auch von Patienten in Anspruch genommen werden, die Pflegegeld in Anspruch nehmen und sich nicht der Hilfe eines Pflegedienstes bedienen. Das Budget wird zusätzlich zum Pflegegeld zur Verfügung gestellt.</p>
      </div>
    </div>
    <div class="brand" style="left:0;right:0;top:330px;gap:6px">
      <span class="brand__dot" style="width:36px;height:36px"></span>
      <span class="brand__name">Pflegedienst<br>Hafenblick</span>
    </div>
    <svg class="photo" style="left:0;top:420px" width="283" height="180" viewBox="0 0 283 180" role="img" aria-label="Foto: junge Frau umarmt eine ältere Dame">
      <defs><linearGradient id="insidePhoto" x1="0" y1="0" x2="1" y2="1">
        <stop offset="0" stop-color="#8fb07a"/><stop offset=".45" stop-color="#efd3c2"/><stop offset="1" stop-color="#d7807a"/></linearGradient></defs>
      <path d="M0 36 Q160 -10 283 150 L283 180 L0 180 Z" fill="url(#insidePhoto)"/>
      <path d="M0 36 Q160 -10 283 150" fill="none" stroke="#1b5fa8" stroke-width="5"/>
    </svg>
  </div>

  <div class="panel">
    <div class="stack" style="top:40px">
      <div class="box box--tag-bottom">
        <p>Da pflegebedürftige Menschen zu sozialem Rückzug und zur körperlichen Versteifung neigen, sind körperliche Aktivitäten wie Bewegungsspiele und eine kontinuierliche uns konsequente Anleitung zur Mobilität besonders wichtig. Dabei hilft nicht nur, mobil zu bleiben und Energie zu lenken. Da Wahrnehmung und Bewegung voneinander Unabhängig sind, fördert Bewegung die Wahrnehmung sowie den Kontakt zur Umwelt und vermindert damit Anspannung, Ängste und Aggressionen.</p>
        <span class="tag tag--blue tag--bottom-left" style="left:-4px">Bewegung</span>
      </div>
      <div class="box box--tag-bottom">
        <p>To ipsandernam reprae aut hario quae cuptae parchiti tem endae di tet, sequia sequam, se porposapiet lantem nonsend latur? Puditaepre, sedis necepudae omnimodis acerum ipsae nes intio molorro consect empelique.</p>
        <p>Cor ra non eum si te modit ium sequiam eicti bla sant volo imendi toribus dandis re, exceped eum facea asitati consequi nis enda diti arumquia sunto tentest eniatur.</p>
        <p>Nulparum, sin et, tempelloriat eum fugiassequi commodia voluptur autentium voluptatus dolore non ra aut opti ducim quam, cus mo occusda sedit dolo et rae.</p>
        <p>Nam sum dunt quia consequis preped ut eseque consequi totatenim faccum, iumenim incturem quosam fugitat escia cus.</p>
        <span class="tag tag--green tag--bottom-left">Lorem Ipsum</span>
      </div>
    </div>
  </div>

  <div class="panel">
    <div class="stack" style="top:42px">
      <div class="box">
        <span class="tag tag--green tag--top-right">Lorem Ipsum</span>
        <p>Otatqui inte evelloratem iocium quidior empore rep udipit lit, id ma eum esto qui toribusa volor sus eos neces vel molest aut mos dolo te nulla cumquibus simus dolupta pon optatur?</p>
        <p>Lupta vollicitia sum laccusd aepratur? Animus pa dolorian volaudita comnitissim digente et anienienia quae pra quis arum que volor mollacc aborum, voluptatia comnias volore volorio acerum non consequ.</p>
        <p>Rore re, cor susto quibus ipsum qua nonest, sin nullabo. Uda ime sed mostiur aceptate re venient uscimi, cuptatur, quosa iliatqui volupta turempel moditam corrum.</p>
      </div>
      <div class="box">
        <span class="tag tag--orange tag--top-right">Lorem Ipsum</span>
        <p>Et escilcim rehenia vendaria consequi totae suntota cuptatem utem quissin cone poreium enihicipsam ressend itasper sperepertas doluptatent escitat essitia nducius et laut etur?</p>
        <p>Em quis est volendu ntincipsa exerem qui velligni similiquide idellor emateni porrorepro qui quassitatur?</p>
        <p>Oditaqui delibusdae. Assum necerup itecepe llupis estrum ne lab in natione eum adignim eium fugitis aut vellis doluptam isimusa periost, aut repelia alit, nobis pa nem volore, vidit id essit aut dolore veri consequo.</p>
      </div>
    </div>
  </div>
</section>

</body>
</html>
```